I need a business card representing my company, VELDRA, it's an artist management and design company. Complete name is "VELDRA Artist Mgmt. + Design Co." I need it to be world class and very appealing, sophisticated and artistically unique.
Updates

Posted an updated Brief please see. I need a business card representing my company, VELDRA, it's an artist management and design company. Complete name is "VELDRA Artist Mgmt. + Design Co." I need it to be world class and very appealing, sophisticated and artistically unique.

Designs look the same

Designs look the same

Target Market(s)

Advertisers, Entertainment Companies, Commercial companies

Industry/Entity Type

Advertising

Contact Information for Business Card

I need a business card representing my company, VELDRA, it's an artist management and design company. Complete name is "VELDRA Artist Mgmt. + Design Co." I need it to be world class and very appealing, sophisticated and artistically unique. One side can be VELDRA Artist Mgmt. + Design Co. and the other my name, Teodoro Lindqvist, my contact telephone: 412.638.2957, email veldraartist@plumora.net, my address: 3264 Harwell Ave. #517 Miami, FL 33184

Font styles to use
Other font styles liked:
• Calibri

Colors
ffffff
0455a3
f37122

Requirements
Must have
• "VELDRA" stand out bigger than the rest of the text.
Nice to have
• Name "VELDRA" can be centered on one side or in the corner or along side edges, just need something cool and different.
Should not have
• I am open just try to keep it clean looking

```html
<!DOCTYPE html>
<html lang="en">
<head>
<meta charset="utf-8">
<title>VELDRA Business Card</title>
<link rel="stylesheet" href="https://fonts.googleapis.com/css2?family=Roboto+Condensed:wght@400;700&display=swap">
<style>
  :root {
    --bg: #d4d4d4;
    --white: #ffffff;
    --navy: #04264f;
    --navy-deep: #031d3d;
    --blue: #0b4f8f;
    --cyan: #2ab6d8;
    --ink: #1b2330;
    --rule: #9aa0a6;
  }
  * { box-sizing: border-box; margin: 0; padding: 0; }
  html, body { width: 1200px; height: 1068px; overflow: hidden; background: var(--bg); }
  .sheet {
    width: 1200px; height: 1068px;
    display: flex; flex-direction: column; align-items: center; justify-content: center;
    gap: 48px;
  }
  .card {
    position: relative; width: 860px; height: 478px; overflow: hidden;
    box-shadow: 0 18px 40px rgba(0,0,0,.28);
  }
  .card svg.card-art { position: absolute; inset: 0; }

  .brand {
    position: absolute; display: flex; align-items: center; gap: 18px;
    font-family: "Roboto Condensed", sans-serif; font-weight: 700; line-height: 1;
  }
  .brand-square { width: 18px; height: 18px; flex: none; }

  /* Back side */
  .card-back { background: linear-gradient(120deg, var(--blue) 0%, var(--navy) 55%, var(--navy-deep) 100%); }
  .card-back .brand { right: 94px; top: 96px; color: var(--white); font-size: 100px; }
  .card-back .brand-square { background: var(--cyan); width: 22px; height: 22px; }

  /* Front side */
  .card-front { background: var(--white); }
  .card-front .brand { left: 88px; top: 100px; color: var(--navy); font-size: 82px; }
  .card-front .brand-square { background: var(--cyan); }
  .divider { position: absolute; left: 461px; top: 83px; width: 2px; height: 116px; background: var(--rule); }
  .contact {
    position: absolute; left: 509px; font-family: "Roboto Condensed", sans-serif;
    font-size: 22px; color: var(--ink); display: flex; align-items: center; gap: 22px;
  }
  .contact svg { width: 26px; height: 26px; flex: none; }
  .contact-phone { top: 104px; }
  .contact-email { top: 146px; }
  .holder {
    position: absolute; right: 484px; top: 276px; text-align: right;
    font-family: "Roboto Condensed", sans-serif; color: var(--white);
  }
  .holder-name { font-size: 30px; font-weight: 700; line-height: 1.1; }
  .holder-role { font-size: 21px; font-weight: 700; }
  .address {
    position: absolute; left: 509px; top: 334px; display: flex; gap: 22px;
    font-family: "Roboto Condensed", sans-serif; font-size: 22px; line-height: 29px; color: var(--white);
  }
  .address svg { width: 26px; height: 34px; flex: none; margin-top: 4px; }
</style>
</head>
<body>
<main class="sheet">

  <section class="card card-back" aria-label="Card back">
    <svg class="card-art" width="860" height="478" viewBox="0 0 860 478" role="img" aria-label="Abstract faceted artwork in layered blues">
      <defs>
        <linearGradient id="facetFill" x1="0" y1="0" x2="1" y2="1">
          <stop offset="0" stop-color="#2a7cb8" stop-opacity=".75"/>
          <stop offset=".55" stop-color="#3a9cc6" stop-opacity=".6"/>
          <stop offset="1" stop-color="#1d5f95" stop-opacity=".2"/>
        </linearGradient>
      </defs>
      <polygon points="0,0 100,0 290,276 800,478 0,478" fill="url(#facetFill)"/>
    </svg>
    <div class="brand">
      <span class="brand-square" aria-hidden="true"></span>
      <span class="brand-name">VELDRA</span>
    </div>
  </section>

  <section class="card card-front" aria-label="Card front">
    <svg class="card-art" width="860" height="478" viewBox="0 0 860 478" aria-hidden="true">
      <defs>
        <radialGradient id="bandGlow" cx=".3" cy=".6" r=".7">
          <stop offset="0" stop-color="#0a63ad"/>
          <stop offset="1" stop-color="#04437f"/>
        </radialGradient>
      </defs>
      <rect x="0" y="299" width="860" height="179" fill="url(#bandGlow)"/>
      <rect x="470" y="294" width="390" height="6" fill="var(--cyan)"/>
      <polygon points="434,254 485,301 421,301" fill="#06344d"/>
      <polygon points="0,254 434,254 405,360 0,360" fill="var(--cyan)"/>
    </svg>

    <div class="brand">
      <span class="brand-square" aria-hidden="true"></span>
      <span class="brand-name">VELDRA</span>
    </div>

    <div class="divider"></div>

    <div class="contact contact-phone">
      <svg viewBox="0 0 24 24" aria-hidden="true"><path fill="#1b2330" d="M6.6 10.8a15.2 15.2 0 0 0 6.6 6.6l2.2-2.2c.3-.3.7-.4 1-.2 1.1.4 2.3.6 3.6.6.6 0 1 .4 1 1V20c0 .6-.4 1-1 1A17 17 0 0 1 3 4c0-.6.4-1 1-1h3.5c.6 0 1 .4 1 1 0 1.3.2 2.5.6 3.6.1.3 0 .7-.2 1z"/></svg>
      <span>412.638.2957</span>
    </div>
    <div class="contact contact-email">
      <svg viewBox="0 0 24 24" aria-hidden="true"><path fill="#1b2330" d="M2 6l10 6 10-6v12H2z"/><path fill="#1b2330" d="M2 4h20v1.5L12 11 2 5.5z"/></svg>
      <span>veldraartist@plumora.net</span>
    </div>

    <div class="holder">
      <div class="holder-name">TEODORO LINDQVIST</div>
      <div class="holder-role">founder/ceo</div>
    </div>

    <div class="address">
      <svg viewBox="0 0 20 26" aria-hidden="true"><path fill="#ffffff" d="M10 0a9 9 0 0 0-9 9c0 6.5 9 17 9 17s9-10.5 9-17a9 9 0 0 0-9-9zm0 12.5A3.5 3.5 0 1 1 10 5.5a3.5 3.5 0 0 1 0 7z"/></svg>
      <div>3264 Harwell<br>Ave. #517 Miami<br>FL 33184</div>
    </div>
  </section>

</main>
</body>
</html>
```